menu tonavera

nesecitamos nuestro menu para restaurante mexicano lo qu ebuscamos es un menu moderno pero ala vez elegante de preferencia fondo negro o cafe y letras blancas o letras visibles con fotos

Target Market(s)

personas de todas edades

Industry/Entity Type

Mexican Restaurant

Font styles to use
Sans Serif

Colors
000000
fbfbfb
ec1f27
fbe7d2

Requirements
Must have
• elegancia, moderno presencia
Nice to have
• portada de menu logotipo con fondo moderno

```html
<!DOCTYPE html>
<html lang="en">
<head>
<meta charset="utf-8">
<title>Tonavera Mexican Restaurant Menu</title>
<link href="https://fonts.googleapis.com/css2?family=Cinzel:wght@400;600;700&family=Open+Sans:wght@700&display=swap" rel="stylesheet">
<style>
  :root{
    --ink:#0d0d0d;
    --paper:#fbfbfb;
    --cream:#fbe7d2;
    --cream-deep:#efd9c2;
    --brand-orange:#e8772e;
    --brand-brown:#6b3a1f;
    --stage:#e4e4e4;
    --grey-box:#8a8a8a;
  }
  *{box-sizing:border-box;margin:0;padding:0}
  html,body{width:1200px;height:1200px;overflow:hidden}
  body{background:var(--stage);font-family:'Cinzel',serif;position:relative}
  .spread{position:absolute;left:220px;width:760px;height:540px;display:flex;box-shadow:0 6px 18px rgba(0,0,0,.18)}
  .spread--outside{top:30px}
  .spread--inside{top:630px}
  .panel{position:relative;width:380px;height:540px;overflow:hidden}

  /* outside back panel */
  .back{background:var(--ink);color:var(--paper)}
  .back .wave{position:absolute;inset:0}
  .back-head{position:absolute;left:22px;top:20px;display:flex;align-items:center;gap:12px;width:220px;border-bottom:1px solid #777;padding-bottom:8px}
  .dot{width:46px;height:46px;border-radius:50%;background:var(--paper)}
  .back-head h2{font-size:15px;font-weight:600;letter-spacing:1px}
  .list{position:absolute}
  .back .list{left:22px;top:92px;width:230px}
  .item{display:flex;justify-content:space-between;align-items:flex-start;margin-bottom:7px}
  .item .name{font-size:13px;font-weight:600;line-height:1.1;letter-spacing:.4px}
  .item .desc{font-size:6.5px;line-height:1.25;opacity:.85;margin-top:1px;max-width:180px}
  .item .price{font-size:10px;white-space:nowrap;margin-left:6px;padding-top:3px}
  .photo-round{position:absolute;left:80px;top:240px;width:200px;height:170px;border-radius:50%;background:radial-gradient(circle,#d9a54e 0%,#b97a2c 55%,#f2f2f2 78%);border:4px solid #f2f2f2}
  .address{position:absolute;left:0;right:0;top:430px;text-align:center;font-size:12px;line-height:1.25;letter-spacing:.5px;font-style:normal}
  .address-rule{position:absolute;left:70px;right:50px;top:510px;border-top:1px solid #777}
  .back .url{position:absolute;left:0;right:0;top:518px;text-align:center;font-size:7px}

  /* cover */
  .cover{background:var(--paper)}
  .cover .photo-top{position:absolute;left:0;top:0}
  .brand{position:absolute;left:0;right:0;top:300px;text-align:center}
  .brand-name{font-size:36px;font-weight:400;color:var(--brand-orange);letter-spacing:2px}
  .brand-tag{font-size:11px;color:var(--brand-brown);margin-top:2px}
  .contact{position:absolute;right:60px;top:420px;text-align:center}
  .phone{font-family:'Open Sans',sans-serif;font-weight:700;font-size:17px;color:var(--ink)}
  .contact .url{font-family:'Open Sans',sans-serif;font-weight:700;font-size:7px;color:var(--ink);margin-top:4px}

  /* inside */
  .inside-left,.inside-right{background:linear-gradient(180deg,var(--cream) 0%,var(--cream-deep) 60%);color:var(--ink)}
  .inside-left .item .desc,.inside-right .item .desc{max-width:260px}
  .photo-band{position:absolute;left:0;right:0;top:0}
  .section-title{font-size:17px;font-weight:600;letter-spacing:1px;margin-bottom:5px}
  .top-list .item{margin-bottom:3px}
  .inside-left .top-list{left:24px;top:96px;width:330px}
  .inside-right .top-list{left:22px;top:110px;width:336px}
  .sub{padding-left:4px}
  .dark-band{position:absolute;left:0;right:0;bottom:0;background:var(--ink);color:var(--paper);display:flex;flex-direction:column;padding:12px 22px 12px 24px}
  .inside-left .dark-band{height:240px}
  .inside-right .dark-band{height:252px;padding:10px 18px 12px}
  .dark-band .list{position:static}
  .dark-band .item{margin-bottom:6px}
  .burritos .list{padding:0 4px}
  .burritos .item{margin-bottom:4px}
  .burritos .section-title{text-align:center;margin-bottom:2px}
  .burritos-note{text-align:center;font-size:6.5px;margin-bottom:6px}
  .extras{margin-top:auto;background:var(--grey-box);color:var(--paper);text-align:center;padding:6px 10px;font-size:7.5px;line-height:1.35}
  .extras strong{display:block;font-size:8.5px;font-weight:600;margin-bottom:3px}
</style>
</head>
<body>

<section class="spread spread--outside">
  <article class="panel back">
    <svg class="wave" width="380" height="540" viewBox="0 0 380 540" aria-hidden="true">
      <path d="M300 0 H380 V470 H330 C360 410 350 330 300 300 C250 270 270 200 300 150 C330 100 300 40 300 0 Z" fill="#f3e4d3"/>
    </svg>
    <header class="back-head"><span class="dot"></span><h2>Lorem Ipsum</h2></header>
    <div class="list">
      <div class="item"><div><div class="name">Refried Beans</div><div class="desc">Buttermilk fried chicken breast, American cheese, lettuce &amp; mayonnaise</div></div><span class="price">$2.00</span></div>
      <div class="item"><div><div class="name">Tortillas</div></div><span class="price">$1.99</span></div>
      <div class="item"><div><div class="name">Enchiladas</div><div class="desc">American cheese, crispy smoky bacon, deep fried pickles, and Rafa's hot sauce</div></div><span class="price">$2.25</span></div>
      <div class="item"><div><div class="name">Chile Relleno de Queso</div><div class="desc">With truffled mayo, crispy smoky bacon and parmesan shavings</div></div><span class="price">$2.25</span></div>
    </div>
    <div class="photo-round" role="img" aria-label="Photo of fried chicken strips with fries and a dip"></div>
    <address class="address">Office 33<br>14 Alder Row<br>Westbridge<br>Mexico<br>W4 7QA</address>
    <div class="address-rule"></div>
    <div class="url">www.sample.com</div>
  </article>

  <article class="panel cover">
    <svg class="photo-top" width="380" height="260" viewBox="0 0 380 260" role="img" aria-label="Photo of a taco salad bowl with guacamole, sour cream and tomatoes">
      <defs><linearGradient id="salad" x1="0" y1="0" x2="1" y2="1"><stop offset="0" stop-color="#c98a3e"/><stop offset=".5" stop-color="#d9c9a4"/><stop offset="1" stop-color="#b4552f"/></linearGradient></defs>
      <path d="M0 0 H380 V170 C320 190 300 240 250 250 C190 260 150 190 80 190 C40 190 15 210 0 230 Z" fill="url(#salad)"/>
    </svg>
    <div class="brand">
      <div class="brand-name">TONAVERA</div>
      <div class="brand-tag">Mexican Restaurant</div>
    </div>
    <div class="contact">
      <div class="phone">+00-000-1111</div>
      <div class="url">www.sample.com</div>
    </div>
  </article>
</section>

<section class="spread spread--inside">
  <article class="panel inside-left">
    <div class="photo-band" role="img" aria-label="Photo of sizzling beef fajitas with peppers" style="height:84px;background:linear-gradient(90deg,#5a2418,#8b3b22 40%,#3a1a12 70%,#6e2c1b)"></div>
    <div class="list top-list">
      <h3 class="section-title">Appetizers</h3>
      <div class="item"><div><div class="name">Guacamole Special</div><div class="desc">6oz signature patty, American cheese, lettuce, kitchen sauce</div></div><span class="price">$8.99</span></div>
      <div class="item"><div><div class="name">Choriqueso</div><div class="desc">With crispy smoky bacon</div></div><span class="price">$8.75</span></div>
      <div class="item"><div><div class="name">Bean Dip</div><div class="desc">With crispy smoky bacon, deep-fried pickles and Rafa's hot sauce</div></div><span class="price">$4.95</span></div>
      <div class="item"><div><div class="name">Guacamole Dip</div></div><span class="price">$4.59</span></div>
      <div class="item"><div><div class="name">Cheese Dip</div></div></div>
      <div class="item sub"><div><div class="name">Small</div></div><span class="price">$7.75</span></div>
      <div class="item sub"><div><div class="name">Large</div></div><span class="price">$8.25</span></div>
      <div class="item"><div><div class="name">Steak and Cheese Fries</div></div></div>
    </div>
    <div class="dark-band">
      <div class="list">
        <h3 class="section-title">Side Orders</h3>
        <div class="item"><div><div class="name">Refried Beans</div><div class="desc">Buttermilk fried chicken breast, American cheese, lettuce</div></div><span class="price">$2.00</span></div>
        <div class="item"><div><div class="name">Tortillas</div></div><span class="price">$1.99</span></div>
        <div class="item"><div><div class="name">Enchiladas</div><div class="desc">American cheese, crispy smoky bacon, deep fried pickles, and Rafa's hot sauce</div></div><span class="price">$2.25</span></div>
        <div class="item"><div><div class="name">Chile Relleno de Queso</div><div class="desc">With truffled mayo, crispy smoky bacon and parmesan shavings</div></div><span class="price">$2.25</span></div>
        <div class="item"><div><div class="name">Quesadilla</div><div class="desc">With house chili, chimichurri and sour cream</div></div><span class="price">$4.59</span></div>
        <div class="item"><div><div class="name">Mexican Style Rice</div></div><span class="price">$2.00</span></div>
      </div>
    </div>
  </article>

  <article class="panel inside-right">
    <div class="photo-band" role="img" aria-label="Photo of a plate with guacamole, lettuce and refried beans" style="height:98px;background:linear-gradient(100deg,#e9dcc8,#9bb35a 45%,#f2efe8 65%,#7a4a2a)"></div>
    <div class="list top-list">
      <div class="item"><div><div class="name">Tostada</div><div class="desc">Dusted in flaky sea salt</div></div><span class="price">$3.59</span></div>
      <div class="item"><div><div class="name">Chimichanga Fajita</div><div class="desc">Topped with American cheese sauce</div></div><span class="price">$5.75</span></div>
      <div class="item"><div><div class="name">Chimichanga</div><div class="desc">Topped with American cheese sauce, Rafa's hot sauce, crispy bacon bits</div></div><span class="price">$4.59</span></div>
      <div class="item"><div><div class="name">Taco (Hard or Soft) Tortilla</div><div class="desc">Topped with American cheese sauce, house chili and chimichurri</div></div><span class="price">$2.49</span></div>
      <div class="item"><div><div class="name">Fajita Quesadilla</div><div class="desc">Rafa's hot sauce, house mayo, truffle mayo, chimichurri</div></div><span class="price">$5.99</span></div>
      <div class="item"><div><div class="name">Chips and Salsa (To Go)</div></div><span class="price" style="font-size:7px;padding-top:0">Small $3.50<br>Large $5.29</span></div>
    </div>
    <div class="dark-band burritos">
      <div class="list">
        <h3 class="section-title">Burritos</h3>
        <p class="burritos-note">All burritos come with beans inside</p>
        <div class="item"><div><div class="name">Beef, Chicken or Beans Burrito</div></div><span class="price">$4.25</span></div>
        <div class="item"><div><div class="name">Burrito Supreme</div><div class="desc">Buttermilk fried chicken breast, American cheese, lettuce</div></div><span class="price">$7.75</span></div>
        <div class="item"><div><div class="name">Burrito Blanco</div><div class="desc">Buttermilk fried chicken breast, American cheese, lettuce</div></div><span class="price">$9.59</span></div>
        <div class="item"><div><div class="name">Shrimp Burrito</div><div class="desc">Buttermilk fried chicken breast, American cheese, lettuce</div></div><span class="price">$10.59</span></div>
        <div class="item"><div><div class="name">Burrito Azteca</div><div class="desc">Buttermilk fried chicken breast, American cheese, lettuce</div></div><span class="price">$10.99</span></div>
      </div>
      <div class="extras"><strong>Each extra ingredient : $1.00</strong>Lettuce, chopped tomatoes, pico de gallo, sour cream, shredded cheese, guacamole, jalapeños, green sauce or cheese dip</div>
    </div>
  </article>
</section>

</body>
</html>
```